Business Card Design needed for logo design project

Our company needs a Business Card Design. Please refer to our original project in the link above.
Dorian Whitlock
Broker

W: Grandvistaestates.com
P: 214-555-0187
F: 267-555-0142
E: dorianwhitlock@ferncrestmail.com
A: North Dallas Office

Name Spelling update , sorry Dorian Whitlock card is double sided

```html
<!DOCTYPE html>
<html lang="en">
<head>
<meta charset="UTF-8">
<title>Grandvista Estates Realty – Business Card</title>
<link href="https://fonts.googleapis.com/css2?family=Cinzel:wght@500&family=Oswald:wght@500&family=Roboto+Condensed:wght@700&display=swap" rel="stylesheet">
<style>
  :root {
    --stage: #e9e6e1;
    --charcoal: #2a2927;
    --charcoal-light: #34322f;
    --accent-green: #1aab5c;
    --rule-green: #1c9b52;
    --green-glow: #1f9e58;
    --green-deep: #0a3a20;
    --green-edge: #061f12;
    --gold: #c7ab7d;
    --cream: #f2e8d2;
  }
  * { margin: 0; padding: 0; box-sizing: border-box; }
  html, body {
    width: 1200px;
    height: 960px;
    overflow: hidden;
    background: var(--stage);
  }
  .canvas {
    position: relative;
    width: 1200px;
    height: 960px;
  }
  .card {
    position: absolute;
    left: 240px;
    width: 720px;
    height: 411px;
    overflow: hidden;
    box-shadow: 0 6px 18px rgba(0,0,0,0.18);
  }

  /* Front side */
  .card--front {
    top: 45px;
    background: radial-gradient(ellipse at 55% 45%, var(--charcoal-light), var(--charcoal) 70%);
  }
  .accent-bar {
    position: absolute;
    width: 66px;
    background: var(--accent-green);
  }
  .accent-bar--left { left: 0; top: 78px; height: 270px; }
  .accent-bar--right { right: 0; top: 160px; height: 265px; }

  .brand {
    position: absolute;
    display: flex;
    flex-direction: column;
    align-items: center;
    gap: 18px;
  }
  .brand__mark {
    width: 18px;
    height: 18px;
    background: var(--gold);
  }
  .brand__name {
    font-family: "Cinzel", serif;
    font-weight: 500;
    color: var(--gold);
    text-align: center;
    letter-spacing: 0.08em;
    line-height: 1.2;
  }
  .card--front .brand {
    left: 50%;
    top: 50%;
    transform: translate(-50%, -50%);
  }
  .card--front .brand__name { font-size: 34px; }

  /* Back side */
  .card--back {
    top: 500px;
    background: radial-gradient(ellipse at 60% 40%, var(--green-glow) 0%, var(--green-deep) 62%, var(--green-edge) 100%);
  }
  .card--back .brand {
    left: 30px;
    width: 230px;
    top: 50%;
    transform: translateY(-50%);
  }
  .card--back .brand__mark { width: 14px; height: 14px; }
  .card--back .brand__name { font-size: 22px; }

  .divider {
    position: absolute;
    left: 285px;
    top: 40px;
    width: 2px;
    height: 330px;
    background: var(--rule-green);
  }
  .contact {
    position: absolute;
    left: 325px;
    top: 52px;
    color: var(--cream);
  }
  .contact__name {
    font-family: "Oswald", sans-serif;
    font-weight: 500;
    font-size: 38px;
    line-height: 1;
    text-transform: uppercase;
    letter-spacing: 0.01em;
  }
  .contact__title {
    font-family: "Oswald", sans-serif;
    font-weight: 500;
    font-size: 27px;
    line-height: 1.15;
    text-transform: uppercase;
    margin-top: 4px;
  }
  .contact__list {
    list-style: none;
    margin-top: 38px;
    font-family: "Roboto Condensed", sans-serif;
    font-weight: 700;
    font-size: 19px;
    line-height: 40px;
  }
</style>
</head>
<body>
<main class="canvas">
  <section class="card card--front" aria-label="Business card front">
    <div class="accent-bar accent-bar--left"></div>
    <div class="accent-bar accent-bar--right"></div>
    <div class="brand">
      <span class="brand__mark"></span>
      <span class="brand__name">Grandvista Estates<br>Realty</span>
    </div>
  </section>

  <section class="card card--back" aria-label="Business card back">
    <div class="brand">
      <span class="brand__mark"></span>
      <span class="brand__name">Grandvista Estates<br>Realty</span>
    </div>
    <div class="divider"></div>
    <div class="contact">
      <h1 class="contact__name">Dorian Whitlock</h1>
      <p class="contact__title">Broker</p>
      <ul class="contact__list">
        <li>W: Grandvistaestates.com</li>
        <li>P: 214-555-0187</li>
        <li>F: 267-555-0142</li>
        <li>E: dorianwhitlock@ferncrestmail.com</li>
      </ul>
    </div>
  </section>
</main>
</body>
</html>
```